Successful Software Co Launching A Super FUN Mobile & Web Application - ROCKSTAR Designer Needed

Our App is called "Sparkle Pennant"It is an employee "gamification" app designed to make working at your job fun...Employees complete simple tasks throughout the work day and are rewarded with points they can redeem for different gifts and benefits...We an AMAZING User Interface designed for both the mobile app and website app. We are looking for a clean, modern and simple design... This app is designed to make employees more engaged at work while having fun doing the things they already do each day...They can then redeem their points for rewards. It needs to be easy to understand and simple in its design...Example: A local carpet cleaning business uses our app.Their employees show up to work on time - They get 50 pointsThey clean out their work vehicle - They get 100 pointsThey up-sell an additional cleaning job - The get 250 pointsEtc...The app will also have fun icons and graphics that appear on the screen when an employee accomplishes a task.The app will play fun music sounds when they accomplish tasks too.
Updates

Need extra days to review

Target Market(s)

Small business owners

Logo Text

Sparkle Pennant

Font styles to use
Sans Serif

Colors

Designer to choose colors to be used in the design.

Requirements
Must have
• Simple elegant design
Nice to have
• I'd like to see examples of fun "icons" that could pop up on the screen after an employee completes a "task" and earns points... Something fun to pop up on the screen... (like a happy face, a thumbs up, fun text bubbles... "Way To Go!" etc... or any other fun ideas)

```html
<!DOCTYPE html>
<html lang="en">
<head>
<meta charset="utf-8">
<title>Perk Parade – Rewards Home</title>
<link href="https://fonts.googleapis.com/css2?family=Pacifico&display=swap" rel="stylesheet">
<style>
  :root {
    --white: #ffffff;
    --ink: #1c1a17;
    --gold: #ffc000;
    --brick: #8e2424;
    --smoke: rgba(40, 38, 36, 0.82);
    --glass: rgba(255, 255, 255, 0.22);
    --panel: rgba(48, 46, 44, 0.55);
    --panel-edge: rgba(255, 255, 255, 0.22);
    --rule: rgba(255, 255, 255, 0.2);
    --script: 'Pacifico', cursive;
  }
  * { box-sizing: border-box; margin: 0; padding: 0; }
  html, body { width: 1200px; height: 2271px; overflow: hidden; }
  body {
    position: relative;
    font-family: var(--script);
    color: var(--white);
    background: #3c4330;
  }
  .hero-photo {
    position: absolute; inset: 0;
    background:
      radial-gradient(ellipse 420px 700px at 300px 1100px, rgba(150,160,190,0.55), transparent 70%),
      radial-gradient(ellipse 500px 900px at 950px 700px, rgba(150,160,70,0.6), transparent 70%),
      linear-gradient(180deg, #6b7a3a 0%, #4f5a30 35%, #4a4638 65%, #2c2a24 100%);
  }
  .hero-shade {
    position: absolute; inset: 0;
    background: linear-gradient(180deg, rgba(0,0,0,0.18) 0%, rgba(0,0,0,0.28) 60%, rgba(0,0,0,0.4) 100%);
  }
  .menu-icon { position: absolute; left: 128px; top: 201px; }
  .settings-icon { position: absolute; left: 1027px; top: 198px; }
  .welcome {
    position: absolute; left: 0; top: 300px; width: 1200px;
    text-align: center; font-size: 78px; line-height: 112px; font-weight: 400;
  }
  .progress-pill {
    position: absolute; left: 102px; top: 616px; width: 1042px; height: 116px;
    border-radius: 58px; background: var(--glass);
    display: flex; align-items: center; justify-content: center;
    font-size: 33px;
  }
  .monthly-goal {
    position: absolute; left: 0; top: 760px; width: 1200px;
    text-align: center; font-size: 62px; line-height: 90px;
  }
  .redeem-button {
    position: absolute; left: 311px; top: 899px; width: 620px; height: 138px;
    border-radius: 69px; background: var(--gold); color: var(--ink);
    display: flex; align-items: center; justify-content: center;
    font-size: 46px;
  }
  .history-title {
    position: absolute; left: 0; top: 1070px; width: 1200px;
    text-align: center; font-size: 50px; line-height: 80px;
  }
  .history-panel {
    position: absolute; left: 77px; top: 1181px; width: 1048px; height: 855px;
    border-radius: 68px; background: var(--panel);
    border: 2px solid var(--panel-edge);
  }
  .task-row {
    position: absolute; left: 37px; width: 980px;
    display: flex; align-items: center; justify-content: space-between;
  }
  .task-row + .task-row::before { content: none; }
  .task-name { font-size: 35px; line-height: 52px; max-width: 640px; padding-left: 18px; }
  .points-badge {
    width: 238px; height: 99px; border-radius: 50px;
    background: var(--gold); color: var(--ink);
    display: flex; align-items: center; justify-content: center;
    font-size: 35px;
  }
  .row-rule { position: absolute; left: 37px; width: 980px; height: 2px; background: var(--rule); }
  .action-button {
    position: absolute; top: 2122px; height: 220px; width: 497px;
    border-radius: 68px; padding-top: 30px;
    text-align: center; font-size: 56px; line-height: 90px;
  }
  .contact-button { left: 107px; background: var(--brick); }
  .timeoff-button { left: 618px; background: var(--smoke); }
</style>
</head>
<body>
  <div class="hero-photo" role="img" aria-label="Blurred photo of a worker in a cap and overalls holding a hose outdoors among green foliage"></div>
  <div class="hero-shade"></div>

  <svg class="menu-icon" width="52" height="40" viewBox="0 0 52 40" aria-label="Menu">
    <g stroke="#fff" stroke-width="3" stroke-linecap="round">
      <line x1="6" y1="2" x2="50" y2="2"/>
      <line x1="2" y1="20" x2="50" y2="20"/>
      <line x1="6" y1="38" x2="50" y2="38"/>
    </g>
  </svg>

  <svg class="settings-icon" width="56" height="56" viewBox="0 0 56 56" aria-label="Settings">
    <g fill="none" stroke="#fff" stroke-width="3" stroke-linejoin="round">
      <path d="M24 4h8l1.5 6 5 2.2 5.4-3.2 5.7 5.7-3.2 5.4 2.2 5 6 1.5v8l-6 1.5-2.2 5 3.2 5.4-5.7 5.7-5.4-3.2-5 2.2-1.5 6h-8l-1.5-6-5-2.2-5.4 3.2-5.7-5.7 3.2-5.4-2.2-5-6-1.5v-8l6-1.5 2.2-5-3.2-5.4 5.7-5.7 5.4 3.2 5-2.2z"/>
      <circle cx="28" cy="28" r="9"/>
    </g>
  </svg>

  <h1 class="welcome">Welcome to Perk Parade,<br>Lorna</h1>

  <div class="progress-pill">you are only 750 points away from your Next Reward</div>

  <div class="monthly-goal">Monthly Goal: 3000 Points</div>

  <div class="redeem-button">Redeem Your Rewards</div>

  <h2 class="history-title">Reward History</h2>

  <section class="history-panel">
    <div class="task-row" style="top:72px;">
      <span class="task-name">Show Up On Time Every Day For 1 Month</span>
      <span class="points-badge">100 Points</span>
    </div>
    <div class="row-rule" style="top:214px;"></div>
    <div class="task-row" style="top:263px;">
      <span class="task-name">Up-Sell over $ 250 In Services</span>
      <span class="points-badge">250 Points</span>
    </div>
    <div class="row-rule" style="top:404px;"></div>
    <div class="task-row" style="top:462px;">
      <span class="task-name">Pass Your Vehicle Inspection Report Each Week</span>
      <span class="points-badge">250 Points</span>
    </div>
    <div class="row-rule" style="top:608px;"></div>
    <div class="task-row" style="top:654px;">
      <span class="task-name">Daily Paperwork Turned In Complete &amp; On Time</span>
      <span class="points-badge">250 Points</span>
    </div>
  </section>

  <div class="action-button contact-button">Contact Employer</div>
  <div class="action-button timeoff-button">Request Time Off</div>
</body>
</html>
```